Career development coaching - school lever to adults, needs a business card

Tandem Lark - An independent Career Advice business that provides 1-2-1 advice,for career development, entrepreneurial support and workshops needs a business card. Our clients of all ages (school leaver to adults looking for a career move) and universities and colleges. We would like the card to be double-sided with a modern, professional look. Looking for something professional yet very creative and original. Want a standard size business card that inspires a second look because it stands out from the rest.

One side of the card to have a design incorporating the logo with Tandem Lark name with the strap line “Helping you find your future” and space for the company website

Other side of the card to the logo/Tandem Lark name and the usual contact information:
Individual Name
Job Title (for example, Director)
Phone number
Email address
Company website address

Facebook, LinkedIn and Twitter links will need to go somewhere (back or front!)

The design will be used for 3 individuals so should be editable so that we can update as needed/as we grow.

Attached is the company logo/colours to be incorporated.

Target Market(s)

1-2-1 advice,for career development, entrepreneurial support and workshops needs a business card. Our clients of all ages (school leaver to adults looking for a career move) and universities and colleges.

Industry/Entity Type

Consulting

Contact Information for Business Card

Individual Name
Phone number
Email address
Company website address

Font styles to use
Sans Serif

Colors
0255a3
3176b5
faa54b
f78f20
85acd3
cfdeed

Requirements
Must have
• use the Tandem Lark Logo in some way - using the colours and the blue/orange palette
• For the logo - hope this makes sense to someone or if they direclty relate to the logo image attached!
• For the Orange:- Pantone 1585 C
• In CMYK : C3 M71 Y100 K0
• For the Blue:- 100% Pantone 7469 C
• In CMYK : C100 M62 Y27 K7
• Please feel free to contact me with any questions for more info
Nice to have
• happy to see any creative designs
Should not have
• Nothing too traditional,

```html
<!DOCTYPE html>
<html lang="en">
<head>
<meta charset="utf-8">
<title>Tandem Lark – Business Card</title>
<link href="https://fonts.googleapis.com/css2?family=Open+Sans:wght@400;600&family=Montserrat:wght@500;600&display=swap" rel="stylesheet">
<style>
  :root {
    --stage: #2b2d31;
    --card-white: #ffffff;
    --brand-blue: #0255a3;
    --band-teal: #13729b;
    --accent-orange: #f78f20;
    --ink: #3a3a3a;
    --ink-dark: #1f1f1f;
  }
  * { box-sizing: border-box; margin: 0; padding: 0; }
  html, body { width: 1200px; height: 900px; overflow: hidden; }
  body {
    background: var(--stage);
    display: flex;
    align-items: center;
    justify-content: center;
    gap: 50px;
    font-family: "Open Sans", sans-serif;
  }
  .card {
    position: relative;
    width: 540px;
    height: 310px;
    border-radius: 22px;
    overflow: hidden;
  }

  /* Contact side */
  .card--contact { background: var(--card-white); }
  .corner-block {
    position: absolute; left: 38px; top: 0;
    width: 62px; height: 48px;
    background: var(--band-teal);
  }
  .top-band {
    position: absolute; left: 318px; top: 58px; right: 0;
    height: 58px;
    background: var(--band-teal);
  }
  .identity { position: absolute; left: 112px; top: 20px; }
  .identity__name {
    font-family: "Montserrat", sans-serif;
    font-weight: 500;
    font-size: 30px;
    letter-spacing: 1px;
    color: var(--ink-dark);
    text-transform: uppercase;
    line-height: 1;
  }
  .identity__name span { color: var(--accent-orange); }
  .identity__role {
    margin-left: 118px;
    margin-top: 4px;
    display: inline-block;
    font-size: 19px;
    color: var(--ink);
    padding-bottom: 2px;
    border-bottom: 3px solid var(--band-teal);
  }
  .contacts {
    position: absolute; left: 34px; top: 132px;
    list-style: none;
  }
  .contacts li {
    display: flex; align-items: center; gap: 10px;
    font-size: 14px; color: var(--ink);
    line-height: 26px;
    white-space: nowrap;
  }
  .contacts svg { width: 14px; height: 14px; fill: none; stroke: var(--ink); stroke-width: 1.6; flex: none; }
  .brand-mark {
    position: absolute; right: 30px; bottom: 22px;
    display: flex; flex-direction: column; align-items: center; gap: 8px;
  }
  .brand-mark__dot {
    width: 34px; height: 34px; border-radius: 50%;
    background: var(--accent-orange);
  }
  .brand-mark__name {
    font-family: "Montserrat", sans-serif;
    font-weight: 600;
    font-size: 22px;
    letter-spacing: 1px;
    line-height: 1;
    text-transform: uppercase;
    color: var(--brand-blue);
    white-space: nowrap;
  }

  /* Brand side */
  .card--brand {
    background: var(--brand-blue);
    display: flex; flex-direction: column; align-items: center; justify-content: center;
  }
  .brand-title {
    font-family: "Montserrat", sans-serif;
    font-weight: 600;
    font-size: 44px;
    letter-spacing: 2px;
    color: var(--card-white);
    text-transform: uppercase;
    line-height: 1;
  }
  .brand-strap {
    margin-top: 10px;
    font-size: 13px;
    letter-spacing: 0.5px;
    color: var(--accent-orange);
    text-transform: uppercase;
  }
  .social {
    position: absolute; right: 26px; bottom: 24px;
    display: flex; gap: 6px;
  }
  .social span {
    width: 22px; height: 22px; border-radius: 50%;
    background: var(--card-white);
  }
</style>
</head>
<body>
  <section class="card card--contact" aria-label="Contact side">
    <div class="corner-block"></div>
    <div class="top-band"></div>
    <div class="identity">
      <h1 class="identity__name">Mara <span>Ellison</span></h1>
      <p class="identity__role">Director</p>
    </div>
    <ul class="contacts">
      <li><svg viewBox="0 0 14 14"><path d="M3 1.5l2 2.5-1.3 1.3a7 7 0 0 0 5 5L10 9l2.5 2-1.5 2A10 10 0 0 1 1 3z"/></svg>+000 55501 2468</li>
      <li><svg viewBox="0 0 14 14"><rect x="1" y="3" width="12" height="8"/><path d="M1 3l6 5 6-5"/></svg>mara@tandemlark-mail.com</li>
      <li><svg viewBox="0 0 14 14"><circle cx="7" cy="7" r="5.5"/><path d="M1.5 7h11M7 1.5c-3 3-3 8 0 11M7 1.5c3 3 3 8 0 11"/></svg>tandemlark-site.com</li>
      <li><svg viewBox="0 0 14 14"><path d="M7 13s-4.5-4.5-4.5-7.5a4.5 4.5 0 0 1 9 0C11.5 8.5 7 13 7 13z"/><circle cx="7" cy="5.5" r="1.5"/></svg>12 Wren Lane, Singapore, 1234</li>
    </ul>
    <div class="brand-mark">
      <span class="brand-mark__dot"></span>
      <span class="brand-mark__name">Tandem Lark</span>
    </div>
  </section>

  <section class="card card--brand" aria-label="Brand side">
    <h2 class="brand-title">Tandem Lark</h2>
    <p class="brand-strap">Helping you find your future</p>
    <div class="social" aria-label="Social links">
      <span></span><span></span><span></span>
    </div>
  </section>
</body>
</html>
```